Modern & Simple Essential Oils Label

Company Name: Verdant Hollow

What we sell: Aromatherapy products, pure therapeutic essential oils.

Design need:
We are looking for a creative and youthful design for the labels used on small essentials oils.

I have two sizes of bottles that I use for essential oils a 5ml bottle and a 15ml bottle. They are dark Amber color glass with black lids. I like the clear labels or mayble a dark brown background. With white or clear lettering with punch of color too! Each oil type is represented by different color. (lavender- purple, lemon - yellow). The label will be the same for all the oils in the two sizes with only a different oil name & coordinating color.
5ml label size should be: 1 " x 2.625"
15ml label size should be: 1.5" x 3.5"

I have some labels that I have had another designer start on, but they aren't quite what I want and missing that something (alot!).. I don't know what. Interest maybe? Lack of design? I dunno.. they are attached. Maybe it's the logo? I don't know! But its gotta change! When I cut out a proof and put a sample on the bottle as I look straight on at the label all I see is a big dot, no logo.. nothing interesting.
Updates

Project Deadline Extended
Reason: Hi! Id like to extend this deadline. Ive been unavailable for a few days due to an illness and Im so far behind! Im feeling MUCH better and looking forward to getting caught up and move with the project. Im not sure how this works, but I attached a list of the oils that we currently have available. And in the list is the idea for the color schemes for the oils. The basic idea is for it to have a wide array of colors, so using different shades of greens, yellows, oranges and so on. So that its like a rainbow. We are not set of that particular color for that particular oil. It was just a idea list of possible colors for oils. Thanks so much!

Target Market(s)

Metro & Modern people. Interested in healthy organic living, Mostly women (some men) 20-45 who are interested in holistic healing.

Industry/Entity Type

It Company

Requirements
Must have
• A reputable look. Clean, organic, crisp, zen or spa-like feel. Modern, youthful appealing label design. Approachable and interesting, not intimidating so that I don't turn away people who are new or not familiar with how to use essential oils.
Should not have
• do NOT want the look to be anywhere close to medicinal, witchy, crafty, hippie, mystical, overly earthy, magical, or voodoo. Do not want it to look like something out of a grandmothers medicine cabinet.

```html
<!DOCTYPE html>
<html lang="en">
<head>
<meta charset="utf-8">
<title>Verdant Hollow – Patchouli Label</title>
<link href="https://fonts.googleapis.com/css2?family=Arimo:wght@400;700&family=Josefin+Sans:wght@300&family=Rosarivo:ital@1&family=Source+Sans+3:wght@400&display=swap" rel="stylesheet">
<style>
  :root {
    --bg-top: #5b3a17;
    --bg-mid: #3a2717;
    --bg-bottom: #1b1b1b;
    --oil: #7b4fe6;
    --oil-light: #b39cf0;
    --ink-dark: #1e1b1f;
    --ink-light: #ffffff;
  }
  * { margin: 0; padding: 0; box-sizing: border-box; }
  html, body { width: 1200px; height: 514px; overflow: hidden; }
  body { font-family: "Source Sans 3", "Helvetica Neue", Arial, sans-serif; color: var(--ink-light); }

  .label {
    position: relative;
    width: 1200px;
    height: 514px;
    background: linear-gradient(180deg, var(--bg-top) 0%, var(--bg-mid) 45%, var(--bg-bottom) 100%);
    overflow: hidden;
  }

  /* Rotated text columns: box keeps its place, text reads bottom to top */
  .vertical {
    position: absolute;
    writing-mode: vertical-rl;
    transform: rotate(180deg);
    text-align: start;
    white-space: nowrap;
    overflow: hidden;
  }

  /* Facts panel */
  .facts-frame {
    position: absolute;
    left: 17px; top: 17px;
    width: 189px; height: 480px;
    border: 3px solid var(--ink-light);
  }
  .facts-strip {
    position: absolute;
    right: 0; top: 0; bottom: 0;
    width: 36px;
    background: var(--ink-light);
  }
  .facts-text {
    left: 30px; top: 24px;
    width: 134px; height: 466px;
    font-family: "Arimo", Arial, sans-serif;
    font-size: 18px;
    line-height: 28px;
  }
  .facts-text strong { font-size: 23px; font-weight: 700; line-height: 32px; }
  .grade-text {
    left: 170px; top: 24px;
    width: 33px; height: 466px;
    font-family: "Arimo", Arial, sans-serif;
    font-size: 17px;
    line-height: 33px;
    color: var(--ink-dark);
  }

  /* Oil panel */
  .oil-panel {
    position: absolute;
    left: 221px; top: 0;
    width: 585px; height: 457px;
    background: var(--oil);
  }
  .brand-name {
    position: absolute;
    left: 0; right: 0; top: 148px;
    text-align: center;
    font-family: "Josefin Sans", sans-serif;
    font-weight: 300;
    font-size: 40px;
    letter-spacing: 2px;
    color: var(--ink-light);
  }
  .oil-band {
    position: absolute;
    left: 0; right: 0; top: 309px;
    height: 85px;
    background: var(--oil-light);
    text-align: center;
    color: var(--ink-dark);
  }
  .oil-name {
    font-family: "Josefin Sans", sans-serif;
    font-weight: 300;
    font-size: 46px;
    letter-spacing: 3px;
    line-height: 46px;
    padding-top: 16px;
  }
  .oil-latin {
    font-family: "Rosarivo", Georgia, serif;
    font-style: italic;
    font-size: 22px;
    letter-spacing: 1.5px;
    line-height: 22px;
  }
  .volume {
    position: absolute;
    left: 221px; width: 585px; top: 467px;
    text-align: center;
    font-size: 21px;
  }

  /* Info columns */
  .company-info { left: 828px; top: 40px; width: 60px;  height: 457px; font-size: 20px; line-height: 24px; }
  .usage-info   { left: 903px; top: 40px; width: 90px;  height: 457px; font-size: 23px; line-height: 26px; }
  .caution-info { left: 1008px; top: 20px; width: 172px; height: 477px; font-size: 23px; line-height: 26.5px; }
</style>
</head>
<body>
<div class="label">

  <div class="facts-frame">
    <div class="facts-strip"></div>
  </div>
  <div class="vertical facts-text">
    <strong>Supplemental Facts</strong><br>
    Serving Size: 1 drop<br>
    Servings Per Container: About 250<br>
    Oil: Pogostemon Cablin
  </div>
  <div class="vertical grade-text">100% Pure Therapeutic Grade</div>

  <div class="oil-panel">
    <div class="brand-name">Verdant Hollow</div>
    <div class="oil-band">
      <div class="oil-name">PATCHOULI</div>
      <div class="oil-latin">pogostemon cablin</div>
    </div>
  </div>
  <div class="volume">15 ml (0.5 US FL OZ)</div>

  <div class="vertical company-info">
    Verdant Hollow<br>
    P.O. Box 204, Maple Ridge, UT 84099
  </div>
  <div class="vertical usage-info">
    For aromatic, topical use. 100% pure<br>
    therapeutic-grade essential oil. Dilute<br>
    with a carrier oil before using.
  </div>
  <div class="vertical caution-info">
    CAUTION: For External Use Only. Not for<br>
    Ingestion. Keep away from eyes and<br>
    mucous membranes. May cause skin<br>
    sensitivity. If pregnant consult physician<br>
    before use. Keep out of reach of children.<br>
    Keep away from flame.
  </div>

</div>
</body>
</html>
```